Letterhead Design for Law Firm

**Edit: I have added the photo of a bottom that I like.

------
We are looking for a re-design of our new letterhead. The letterhead is for a law firm and will be used for digital and traditionally printed correspondence.

Here are some suggestions:

- Please use colours are #8ec900 and simple black.
- Please do not use any type of "waves" at the bottom of the page. This is not in style at all.
- Please stay modern yet conservative.
- Please use font Segoe UI Light or similar if you can
- Avoid clipart or illustrations.
- Utilize ample white space in the layout so the design looks clean and information is easy to read at a glance. Don't overcrowd the letterhead.
- Make sure the letterhead design is consistent with our brand identity (see brambleford.ca)
-Please, no black headers or footers.

I am attaching my current letterhead and signature for your convenience.

Remember, the letterhead is an extension of our professional identity. We are a successful firm and trial lawyers who correspond with insurers, judges, lawyers, courts, clients, etc. Make it new, modern, attractive, yet powerful and conservative.

It needs to be easily printable. I would like the bleed removed in print so the black bar the bottom crosses the page (but the text is not near the edges)

Target Market(s)

Clients, Government Offices, Judiciary, Lawyers, Insurance Companies, Colleagues.

Industry/Entity Type

Law

Font styles to use
Other font styles liked:
• Segoe UI LIght, Calibri Light,

Colors
00AB8E
00BBA5
67D7C9
C6EFE9
E9F9F6

Requirements
Must have
• Everything that is on the letterhead now.
Nice to have
• Cutting Edge design, yet conservative.
Should not have
• law firm cliche design, images,

```html
<!DOCTYPE html>
<html lang="en">
<head>
<meta charset="utf-8">
<title>Brambleford Letterhead</title>
<link rel="stylesheet" href="https://fonts.googleapis.com/css2?family=Roboto:wght@300;400;500&family=Arimo&family=Playfair+Display:wght@500&display=swap">
<style>
:root{
  --green:#8ec900;
  --ink:#1a1a1a;
  --muted:#555;
  --paper:#f6f4f4;
  --backdrop:#e4e4e4;
  --bar:#1c1c1c;
}
*{margin:0;padding:0;box-sizing:border-box}
html,body{width:935px;height:1200px;overflow:hidden;background:var(--backdrop)}
.page{position:absolute;left:41px;top:0;width:853px;height:1200px;background:var(--paper);font-family:'Roboto',sans-serif;color:var(--ink);font-weight:300}
.abs{position:absolute}
.brand{left:0;width:853px;top:40px;text-align:center;color:var(--ink)}
.brand-name{font-family:'Roboto',sans-serif;font-weight:400;font-size:50px;letter-spacing:1px;line-height:1}
.brand-tag{font-family:'Roboto',sans-serif;font-weight:400;font-size:15px;letter-spacing:2px;margin-top:8px}
.label{font-weight:500;font-size:15.5px}
.right{text-align:right;right:58px}
.clerk{top:152px;font-size:16px}
.clerk b{font-weight:500}
.clerk span{color:var(--muted);font-weight:400}
.date{top:205px;font-size:15px;font-weight:400}
.address{left:40px;top:239px;font-size:16.5px;line-height:20px}
.attn{left:40px;top:363px;font-size:16.5px}
.salute{left:40px;top:391px;font-size:16.5px}
.re-label{left:40px;top:429px}
.re-body{left:298px;top:429px;font-size:16.5px;line-height:20px}
.rule{left:50px;top:513px;width:746px;height:1px;background:#333}
.body{left:50px;width:746px;font-family:'Arimo',sans-serif;font-size:13.6px;line-height:20.5px;color:#444;text-align:justify}
.p1{top:546px}.p2{top:670px}.p3{top:771px}
.closing{left:55px;top:846px;font-size:14.5px;line-height:17.7px;font-weight:400}
.signature{left:55px;top:884px;width:230px;height:60px;background:linear-gradient(90deg,#e6e4e4,#d9d7d7)}
.signer{left:59px;top:969px;font-size:14.5px;line-height:17.7px;font-weight:400}
.tab{width:13px;height:86px;background:var(--green)}
.tab-left{left:0;top:1063px;border-radius:0 8px 8px 0}
.tab-right{right:0;top:1055px;border-radius:8px 0 0 8px}
.contacts{left:61px;top:1077px;font-size:14px;line-height:19px;font-weight:400;list-style:none}
.contacts li{display:flex;align-items:center;gap:6px}
.contacts svg{width:12px;height:12px;fill:var(--green)}
.practice{top:1080px;font-size:14.5px;line-height:19.5px;color:var(--muted);font-weight:400}
.practice b{font-weight:500;color:#333}
.footer-bar{left:0;bottom:0;width:853px;height:35px;background:var(--bar);color:#fff;font-size:15.5px;font-weight:400;display:flex;align-items:center;justify-content:center}
</style>
</head>
<body>
<div class="page">
  <header class="abs brand">
    <div class="brand-name">BRAMBLEFORD</div>
    <div class="brand-tag">PERSONAL INJURY LAWYERS</div>
  </header>

  <div class="abs label" style="left:40px;top:150px">Without Prejudice</div>
  <div class="abs right clerk"><b>File Clerk:</b> <span>Clara Whitfield</span></div>
  <div class="abs label" style="left:40px;top:199px">By Email</div>
  <div class="abs right date">March 13, 2024</div>

  <address class="abs address" style="font-style:normal">
    Northvale Insurance Company<br>
    Claims Litigation Department<br>
    240 Orchard Road South<br>
    P.O. Box 4100<br>
    Waterloo, ON &nbsp; N2A 0B1
  </address>

  <div class="abs attn">Attention:&nbsp; Mr. Dale Morrow</div>
  <div class="abs salute">Mr. Morrow:</div>

  <div class="abs label re-label">Re:</div>
  <div class="abs re-body">
    Harlow v. Penner et al.<br>
    DOL:&nbsp; September 12, 2019<br>
    Pre-Mediation Settlement Proposal – March 13th, 2024
  </div>

  <div class="abs rule"></div>

  <p class="abs body p1">Lorem ipsum dolor sit amet, consectetur adipiscing elit. Donec orci purus, luctus vitae dignissim eu, iaculis sed purus. Vivamus faucibus, ipsum nec aliquet viverra, leo mauris condimentum ligula, sit amet sagittis enim ligula quis arcu. Nam egestas tortor ivisi porttitor mattis. In tortor ante, ultricies in suscipit a, tempus non massa. Vivamus et auctor mi. Fusce vel massa nulla. Phasellus nec eros mauris, et scelerisque orci.</p>
  <p class="abs body p2">Donec malesuada orci vitae nulla accumsan porta a id massa. Quisque accumsan iaculis magna sit amet fringilla. Maecenas consequat, magna eget tincidunt semper, odio nibh rutrum mi, id feugiat ante nisi eu risus. Vestibulum nunc orci, rhoncus a placerat in, ultricies in mi. Cras mattis varius eros, vel fringilla nisi suscipit eget. Quisque scelerisque sagittis nulla at porttitor.</p>
  <p class="abs body p3">Sed id augue vitae urna euismod commodo aliquet a quam. Pellentesque arcu velit, cursus et malesuada ut, consequat et diam. Nullam erat sem, rhoncus id ullamcorper vitae, rhoncus et arcu. In ultricies ultricies nulla, ut rutrum nisi iaculis</p>

  <div class="abs closing">Yours very truly,<br>BRAMBLEFORD PERSONAL INJURY LAWYERS</div>
  <div class="abs signature" role="img" aria-label="Handwritten signature of Owen R. Brambleford"></div>
  <div class="abs signer">Owen R. Brambleford<br>Brambleford Law Professional Corporation<br>/cw<br>Encl.</div>

  <div class="abs tab tab-left"></div>
  <div class="abs tab tab-right"></div>

  <ul class="abs contacts">
    <li><svg viewBox="0 0 12 12"><path d="M2.5 0.5l2 2-1 1.5c.6 1.6 1.9 2.9 3.5 3.5l1.5-1 2 2-1.2 2C5 12 0 7 .5 1.7z"/></svg>905-555-0142</li>
    <li><svg viewBox="0 0 12 12"><rect x="3" y="0.5" width="6" height="3"/><rect x="0.5" y="4" width="11" height="5" rx="1"/><rect x="3" y="8" width="6" height="3.5"/></svg>905-555-0178</li>
    <li><svg viewBox="0 0 12 12"><rect x="0.5" y="2.5" width="11" height="7.5"/><path d="M0.5 2.5L6 7l5.5-4.5" stroke="#fff" stroke-width="1" fill="none"/></svg>Email: clara@brambleford.ca</li>
    <li><svg viewBox="0 0 12 12"><circle cx="6" cy="6" r="5.5"/><path d="M1 6h10M6 .5c-2.5 3-2.5 8 0 11M6 .5c2.5 3 2.5 8 0 11" stroke="#fff" stroke-width=".8" fill="none"/></svg>www.BRAMBLEFORD.ca</li>
  </ul>

  <div class="abs right practice">
    <b>Practice Restricted-</b> Serious Personal Injury, Wrongful Death Litigation<br>
    Long-Term Disability Litigation, Wrongful Dismissal Litigation<br>
    Employee Terminations
  </div>

  <footer class="abs footer-bar">18 Market Street W., Suite 1705, Hamilton, ON &nbsp;L8P 0A1</footer>
</div>
</body>
</html>
```